We need a complete design for our construction company KELSO CONSTRUCTION based in Auckland New Zealand, we need a logo, website, business card, vehicle design etc..
We are a mid to high-end construction company who work mostly on residential projects and some commercial.

What we want to see in the design;
Professional,
Architectural,
Simple,
Alternative,

We want the design to communicate professionalism, high quality wormanship and and quality service.

Target Market(s)

People looking for a quality building/ construction company

Industry/Entity Type

Construction Company

Contact Information for Business Card

KELSO CONSTRUCTION.co.nz
Remi Tulvane
remi@kelsoconstruction-example.co.nz
021 5870 463

Logo Text

KELSO CONSTRUCTION

Number of Pages Required

5+ page

Font styles to use
Sans Serif

Colors

Designer to choose colors to be used in the design.

Requirements
Must have
• Must appear high end, professional, quality, be simple, easy to use, give security to potential clients
Nice to have
• high-quality photos of our recent projects
• about us page
• blog page
• contact us page
• high quality content
Should not have
• should not be hard to use and have too much going on.

```html
<!DOCTYPE html>
<html lang="en">
<head>
<meta charset="utf-8">
<title>Kelso Construction – Brand Identity</title>
<link rel="stylesheet" href="https://fonts.googleapis.com/css2?family=Montserrat:wght@400;500;600;700;800&family=Open+Sans:wght@400;600&display=swap">
<style>
:root{
  --blue:#0f66ae;
  --bright:#1386dd;
  --navy:#2e384b;
  --ink:#333b4b;
  --slate:#5c616d;
  --pale:#eef1f5;
  --white:#ffffff;
}
*{box-sizing:border-box;margin:0;padding:0}
html,body{width:1200px;height:1200px;overflow:hidden;background:var(--white)}
body{font-family:"Open Sans",sans-serif;color:var(--ink)}
.canvas{position:relative;width:1200px;height:1200px;overflow:hidden}
.backdrop{position:absolute;inset:0}
.abs{position:absolute}
.wordmark{font-family:"Montserrat",sans-serif;font-weight:800;line-height:.95;text-align:center}
.wordmark .big{display:block}
.wordmark .small{display:block;letter-spacing:.01em}

/* logo presentation */
.logo-main{left:120px;top:215px;width:372px;color:var(--blue)}
.logo-main .big{font-size:80px}
.logo-main .small{font-size:29px;margin-top:4px}
.logo-mini{left:200px;top:412px;width:212px;color:var(--navy)}
.logo-mini .big{font-size:44px}
.logo-mini .small{font-size:16px;margin-top:2px}

/* website mockup */
.site{left:769px;top:66px;width:325px;height:1120px;background:var(--white);overflow:hidden}
.site section,.site header,.site footer{position:absolute;left:0;width:325px;overflow:hidden}
.site-header{top:0;height:30px;background:var(--white);border-bottom:3px solid var(--navy)}
.site-header .brand{left:42px;top:5px;font-family:"Montserrat",sans-serif;font-weight:800;font-size:8px;line-height:1;color:var(--blue)}
.site-header .phone{left:208px;top:6px;font-size:4px;color:var(--ink)}
.site-header .cta{left:246px;top:4px;width:38px;height:8px;background:var(--bright);color:var(--white);font-size:3.5px;text-align:center;line-height:8px}
.site-header nav{position:absolute;left:200px;top:18px;font-size:4px;color:var(--ink);display:flex;gap:6px}
.tiny{font-size:4px;line-height:1.35}
.hero{top:30px;height:331px;background:var(--white)}
.hero .welcome{left:42px;top:22px;font-family:"Montserrat",sans-serif;font-weight:800;font-size:9px;line-height:1.2;color:var(--navy)}
.hero .welcome span{color:var(--blue)}
.hero .intro{left:42px;top:47px;width:130px;color:var(--ink)}
.hero-visual{left:22px;top:10px;width:298px;height:225px;border-radius:40% 30% 10% 20%;background:radial-gradient(ellipse at 45% 55%,#f2f3f5 0 30%,#1782db 55%,rgba(255,255,255,0) 72%)}
.hero .about{right:42px;top:262px;width:170px;text-align:right;color:var(--white)}
.hero .about h3{font-family:"Montserrat",sans-serif;font-size:10px;line-height:1}
.hero .about h4{font-family:"Montserrat",sans-serif;font-size:7px;margin-bottom:6px}
.how{top:361px;height:197px;background:linear-gradient(90deg,#3b3e44,#2a2c31 60%,#4a4d53)}
.how .copy{left:42px;top:57px;width:95px;color:var(--white)}
.how h3{font-family:"Montserrat",sans-serif;font-size:9px}
.how .sub{font-size:4px;color:#4aa7f0;margin:3px 0 6px}
.how .btn{margin-top:8px;display:inline-block;border:1px solid var(--white);font-size:3.5px;padding:2px 5px}
.how .steps{left:153px;top:58px;width:10px;height:96px}
.tablet{left:158px;top:15px;width:125px;height:162px;border-radius:6px;background:#111;border:2px solid #bbb}
.tablet .screen{position:absolute;left:10px;top:14px;width:101px;height:128px;background:var(--bright);padding:14px 10px;color:var(--white);text-align:center}
.tablet .screen b{font-family:"Montserrat",sans-serif;font-size:8px;display:block;line-height:1}
.tablet .field{height:5px;border:.6px solid rgba(255,255,255,.8);margin-top:4px}
.satisfy{top:558px;height:86px;background:linear-gradient(180deg,#e6eaef,#c4ccd6);text-align:center}
.satisfy h3{font-family:"Montserrat",sans-serif;font-size:10px;line-height:1.2;color:var(--navy);margin-top:18px}
.satisfy h3 span{color:var(--bright)}
.satisfy p{width:160px;margin:2px auto 0}
.team{top:644px;height:78px;background:linear-gradient(90deg,#2d2f33,#45474b,#2d2f33);text-align:center;color:var(--white)}
.team h3{font-family:"Montserrat",sans-serif;font-size:7.5px;line-height:1.3;margin-top:20px}
.team .btn{display:inline-block;border:1px solid var(--white);font-size:3.5px;padding:2px 5px;margin-top:4px}
.about-band{top:722px;height:160px;background:var(--bright);color:var(--white)}
.about-band h3{position:absolute;left:43px;top:36px;font-family:"Montserrat",sans-serif;font-size:9.5px}
.about-band .copy{left:43px;top:52px;width:140px}
.about-band .quote{left:43px;top:125px;font-family:"Montserrat",sans-serif;font-weight:700;font-size:6px}
.about-band .mark{left:186px;top:70px;width:120px;color:var(--white)}
.about-band .mark .big{font-size:24px}
.about-band .mark .small{font-size:9px}
.estimate{top:882px;height:184px;background:linear-gradient(135deg,#2b2d31,#3f4247 60%,#2b2d31);color:var(--white)}
.estimate h3{position:absolute;left:57px;top:27px;font-family:"Montserrat",sans-serif;font-size:8px}
.estimate .cols{left:75px;top:56px;display:flex;gap:20px}
.estimate .cols b{font-size:4px;display:block}
.estimate .input{position:absolute;height:7px;background:var(--white);color:#777;font-size:3px;padding:1px 3px}
.estimate .next{left:75px;top:146px;width:28px;height:8px;background:var(--bright);font-size:3.5px;text-align:center;line-height:8px}
.estimate .progress{left:138px;top:146px;display:flex;gap:8px;align-items:center;font-size:3.5px}
.site-footer{top:1066px;height:54px;background:var(--white)}
.site-footer .legal{left:56px;top:12px;color:var(--ink)}
.site-footer .social{left:56px;top:32px;display:flex;gap:3px}
.site-footer .social i{width:6px;height:6px;border-radius:50%;background:var(--bright);display:block}

/* business cards */
.card{position:absolute;left:114px;width:387px;height:232px;background:var(--pale);overflow:hidden}
.card-one{top:694px}
.card-two{top:942px}
.card-one .logo{left:0;top:36px;width:387px;color:var(--blue)}
.card-one .logo .big{font-size:38px}
.card-one .logo .small{font-size:16px;margin-top:2px}
.card-one .name-tab{left:0;top:116px;width:195px;height:45px}
.name-text{font-family:"Montserrat",sans-serif;color:var(--white);line-height:1.2}
.name-text b{font-size:14px;font-weight:700;display:block}
.name-text span{font-size:14px;font-weight:400}
.card-one .name-text{left:42px;top:124px}
.card-one .address{left:200px;top:139px;font-size:11px;color:var(--slate);display:flex;align-items:center;gap:6px;white-space:nowrap}
.card-band{position:absolute;left:0;width:387px;background:var(--slate);color:#e9ebef;font-size:10px}
.card-one .card-band{top:160px;height:72px}
.contact{position:absolute;display:flex;align-items:center;gap:6px;white-space:nowrap;line-height:1}
.card-two .logo{left:24px;top:40px;width:140px;color:var(--blue)}
.card-two .logo .big{font-size:34px}
.card-two .logo .small{font-size:13px;margin-top:2px}
.card-two .name-text{right:27px;top:40px;text-align:right}
.card-two .tagline{position:absolute;left:0;top:120px;width:387px;height:26px;background:#e2e6ec;font-family:"Montserrat",sans-serif;font-weight:600;font-size:9.4px;color:var(--bright);line-height:26px;padding-left:29px;white-space:nowrap}
.card-two .card-band{top:146px;height:86px}
.ticks{position:absolute;display:grid;grid-template-columns:168px 170px;row-gap:7px;left:27px;top:16px}
.ticks span{display:flex;align-items:center;gap:6px;white-space:nowrap}

.panel-label{font-family:"Montserrat",sans-serif;font-weight:700;font-size:21px;white-space:nowrap}
</style>
</head>
<body>
<div class="canvas">

  <svg class="backdrop" width="1200" height="1200" viewBox="0 0 1200 1200" aria-hidden="true">
    <polygon points="696,0 1200,0 1200,200 640,472" fill="var(--blue)"/>
    <polygon points="0,784 1200,200 1200,1200 0,1200" fill="var(--navy)"/>
  </svg>

  <!-- logo presentation -->
  <h2 class="abs panel-label" style="left:246px;top:61px;color:var(--ink)">Logo Design</h2>
  <div class="abs wordmark logo-main"><span class="big">KELSO</span><span class="small">CONSTRUCTION</span></div>
  <div class="abs wordmark logo-mini"><span class="big">KELSO</span><span class="small">CONSTRUCTION</span></div>

  <!-- website presentation -->
  <h2 class="abs panel-label" style="left:766px;top:28px;color:var(--white)">Website Design</h2>

  <div class="abs site">
    <header class="site-header">
      <div class="abs brand">KELSO<br><span style="font-size:4px">CONSTRUCTION</span></div>
      <div class="abs phone">+1 000 000 0000</div>
      <div class="abs cta">Get Started Now</div>
      <nav><span>Home</span><span>Our Services</span><span>About Us</span><span>Contact</span></nav>
    </header>

    <section class="hero">
      <div class="abs hero-visual" role="img" aria-label="Illustration of a small house on a blue rising arrow"></div>
      <svg class="abs" style="left:0;top:0" width="325" height="331" aria-hidden="true">
        <polygon points="0,250 325,122 325,331 0,331" fill="var(--bright)"/>
      </svg>
      <div class="abs welcome">WELCOME TO<br><span>KELSO CONSTRUCTION</span></div>
      <p class="abs tiny intro">Everyday we pride ourselves on providing our customers with superior service and outstanding value. Home Construction has been a respected provider of construction services.</p>
      <div class="abs about">
        <h3>About us</h3>
        <h4>Kelso Construction</h4>
        <p class="tiny">We plan, build and finish quality homes across Auckland with care, honest pricing and trusted crews. Every project is managed from first sketch to final handover, with clear timelines, tidy sites and regular updates. Our builders bring years of residential and commercial skill, so clients feel secure at every stage and proud of the finished result.</p>
      </div>
    </section>

    <section class="how" role="img" aria-label="Photo of builders in hard hats reviewing a site">
      <div class="abs copy">
        <h3>Here’s how it works</h3>
        <p class="sub">100% Free Signup Process</p>
        <p class="tiny">Our signup process is simple and free. After you submit, we verify your company details and run background checks so only trusted builders join. Once approved you can set pricing, add areas and start receiving leads from local clients.</p>
        <span class="btn">Signup Now</span>
      </div>
      <div class="abs tablet">
        <div class="screen">
          <b>KELSO</b><span style="font-size:3.5px">CONSTRUCTION</span>
          <div class="field"></div><div class="field"></div><div class="field"></div><div class="field"></div>
          <div class="field" style="width:24px;background:#fff;margin:5px auto 0"></div>
          <p style="font-size:3px;margin-top:5px">By signing up you agree to our terms</p>
        </div>
      </div>
      <svg class="abs steps" width="10" height="96" aria-hidden="true">
        <line x1="5" y1="4" x2="5" y2="92" stroke="#fff" stroke-width=".8"/>
        <g fill="var(--bright)" stroke="#fff" stroke-width=".8">
          <circle cx="5" cy="4" r="4"/><circle cx="5" cy="26" r="4"/><circle cx="5" cy="48" r="4"/><circle cx="5" cy="70" r="4"/><circle cx="5" cy="92" r="4"/>
        </g>
      </svg>
    </section>

    <section class="satisfy" role="img" aria-label="Photo of a yellow hard hat in front of a city skyline">
      <h3>THE ULTIMATE IN<br><span>CONTRACTOR SATISFACTION</span></h3>
      <p class="tiny">clear files are created, payments are built in, no money wasted on bad leads, no sales staff, simple steps to build and get paid</p>
    </section>

    <section class="team" role="img" aria-label="Dark photo of a builder on site">
      <h3>Team up with<br>Kelso Construction today!</h3>
      <p style="font-size:3.5px">Just fill out our online application to get started.</p>
      <span class="btn">Get Started Now</span>
    </section>

    <section class="about-band">
      <h3>About Kelso Construction</h3>
      <p class="abs tiny copy">We started with one small crew and a simple promise: build every home as if it were our own. Today our team delivers residential and light commercial projects across Auckland, pairing modern methods with careful craftsmanship. We listen first, quote clearly and keep you informed, so each build runs on time and on budget.</p>
      <p class="abs tiny" style="left:43px;top:115px"><b>Marta Lindqvist,</b><br>Founder and CEO of Kelso Construction</p>
      <p class="abs quote">Let me show you the future of Construction!</p>
      <div class="abs wordmark mark"><span class="big">KELSO</span><span class="small">CONSTRUCTION</span></div>
    </section>

    <section class="estimate" role="img" aria-label="Dark photo of a builder working">
      <h3>Get Your Fast, Free Estimate</h3>
      <p class="abs" style="left:57px;top:40px;font-size:3px">Send us a few details and we will reply with a clear quote.</p>
      <div class="abs cols tiny">
        <div><b>Address Info</b>61 Tui Road<br>Greenlane<br>Auckland 1061</div>
        <div><b>Contact Details</b>+1 000 000 0000<br>info@kelso-example.co.nz</div>
        <div><b>Working Time</b>Mon–Fri 8am–6pm<br>Sunday Closed</div>
      </div>
      <div class="input" style="left:75px;top:84px;width:64px">Your Name</div>
      <div class="input" style="left:143px;top:84px;width:64px">Your Email</div>
      <div class="input" style="left:211px;top:84px;width:64px">Mobile Number</div>
      <div class="input" style="left:75px;top:96px;width:200px;height:35px">Write your message</div>
      <div class="abs next">NEXT</div>
      <div class="abs progress">
        <svg width="7" height="7"><circle cx="3.5" cy="3.5" r="3.3" fill="var(--bright)"/><path d="M2 3.6l1.1 1.1L5.2 2.6" stroke="#fff" stroke-width=".8" fill="none"/></svg><span>PERSONAL INFO</span>
        <svg width="7" height="7"><circle cx="3.5" cy="3.5" r="3" fill="none" stroke="#fff" stroke-width=".7"/></svg><span>ENTER ZIP</span>
        <svg width="7" height="7"><circle cx="3.5" cy="3.5" r="3" fill="none" stroke="#fff" stroke-width=".7"/></svg><span>PROPERTY INFO</span>
      </div>
    </section>

    <footer class="site-footer">
      <svg class="abs" style="left:0;top:-14px" width="325" height="16" aria-hidden="true"><polygon points="0,14 80,4 240,10 325,0 325,16 0,16" fill="var(--white)"/></svg>
      <p class="abs tiny legal">© Copyright 2019 · Kelso Construction · All Rights Reserved<br>Sitemap | Terms &amp; Conditions | Privacy Policy<br>Follow Us On</p>
      <div class="abs social"><i></i><i></i><i></i><i></i></div>
      <span class="abs" style="right:41px;top:0;width:7px;height:7px;background:var(--bright)"></span>
    </footer>
  </div>

  <!-- business card presentation -->
  <h2 class="abs panel-label" style="left:301px;top:625px;width:200px;text-align:right;color:var(--white);line-height:1.12">Business<br>Card Design</h2>

  <div class="card card-one">
    <div class="abs wordmark logo"><span class="big">KELSO</span><span class="small">CONSTRUCTION</span></div>
    <svg class="abs name-tab" width="195" height="45" aria-hidden="true"><polygon points="0,0 195,0 180,45 0,45" fill="var(--bright)"/></svg>
    <div class="abs name-text"><b>Rowan Hale</b><span>Director</span></div>
    <div class="abs address">
      <svg width="9" height="12" viewBox="0 0 9 12"><path d="M4.5 0C2 0 0 2 0 4.5 0 8 4.5 12 4.5 12S9 8 9 4.5C9 2 7 0 4.5 0z" fill="var(--bright)"/><circle cx="4.5" cy="4.5" r="1.6" fill="#fff"/></svg>
      PO Box 418 Auckland 1061
    </div>
    <div class="card-band">
      <div class="contact" style="left:42px;top:12px"><svg width="10" height="10"><rect x="1" y="1" width="8" height="8" rx="1" fill="none" stroke="var(--bright)"/></svg>+0 000 000 0000</div>
      <div class="contact" style="left:205px;top:12px"><svg width="10" height="10" viewBox="0 0 10 10"><path d="M2 0l2 2.5-1 1.2c.6 1.3 1.6 2.3 3 3l1.2-1L10 8l-1.5 2C4 9.5.5 6 0 1.5z" fill="var(--bright)"/></svg>+0 000 000 0000</div>
      <div class="contact" style="left:42px;top:31px"><svg width="11" height="9"><rect x=".5" y=".5" width="10" height="8" fill="none" stroke="var(--bright)"/><path d="M.5 .5l5 4 5-4" fill="none" stroke="var(--bright)"/></svg>rowan@kelsoconstruction-example.co.nz</div>
      <div class="contact" style="left:42px;top:50px"><svg width="11" height="11"><circle cx="5.5" cy="5.5" r="5" fill="none" stroke="var(--bright)"/><ellipse cx="5.5" cy="5.5" rx="2" ry="5" fill="none" stroke="var(--bright)"/><line x1=".5" y1="5.5" x2="10.5" y2="5.5" stroke="var(--bright)"/></svg>www.kelsoconstruction-example.co.nz</div>
    </div>
  </div>

  <div class="card card-two">
    <svg class="abs" style="left:0;top:0" width="387" height="120" aria-hidden="true">
      <polygon points="338,18 387,18 387,120 292,120" fill="var(--slate)"/>
      <polygon points="230,32 387,32 387,78 245,78" fill="var(--bright)"/>
    </svg>
    <div class="abs wordmark logo"><span class="big">KELSO</span><span class="small">CONSTRUCTION</span></div>
    <div class="abs name-text"><b>Tane Ellery</b><span>Director</span></div>
    <div class="tagline">Kelso Construction has been a respected provider of construction services.</div>
    <div class="card-band">
      <div class="ticks">
        <span><svg width="10" height="8"><path d="M1 4l3 3 5-6" stroke="var(--bright)" stroke-width="1.6" fill="none"/></svg>Quality Residential Builds</span>
        <span><svg width="10" height="8"><path d="M1 4l3 3 5-6" stroke="var(--bright)" stroke-width="1.6" fill="none"/></svg>Quality Residential Builds</span>
        <span><svg width="10" height="8"><path d="M1 4l3 3 5-6" stroke="var(--bright)" stroke-width="1.6" fill="none"/></svg>Commercial Projects</span>
        <span><svg width="10" height="8"><path d="M1 4l3 3 5-6" stroke="var(--bright)" stroke-width="1.6" fill="none"/></svg>Commercial Projects</span>
        <span><svg width="10" height="8"><path d="M1 4l3 3 5-6" stroke="var(--bright)" stroke-width="1.6" fill="none"/></svg>Renovations and Extensions</span>
      </div>
    </div>
  </div>

</div>
</body>
</html>
```